Home Page for Ventrova

We need to design a new home page for Prospix.com, a provider of B2B data for sales and marketing professionals.

The home page should follow the lead of our newly re-designed header and logo (still being tweaked) and use our new color scheme. Please refer to attached file. Please use this file as as the basis of the design for the rest or the home page. No part of the header or logo needs to be altered in this project.

All submissions should be clear, fresh, clean and simple in style. We like the look and feel of tallyvine.com, costharbor.com and pollquarry.com. Please use them as references.

The main functions of the home page will be to tell the user about 1) the benefits and uses of Ventrova and 2) to get them to sign up.

Based upon the successful redesign of our homepage, we will also be redesigning our subscription page and our about us page in the coming weeks.

Target Market(s)

Sales and marketing professionals. Mostly 25 - 45 year old males.

Industry/Entity Type

Marketing

Requirements
Must have
• Items needed:

1A) There should be three main points highlighted 1) Fresh Data 2) Sales Intelligence 3) Increased Bottomline. There will be further text under these headers tbd. For style/feel reference the same device used by pollquarry uses on its homepage.

1B) When you rollover these three items they should highlight and be clickable. The click will lead you to a header and paragraph about each that is further down the homepage (text tbd).

2) We also need a free trial and a sign up button. This button should move with you as you scroll up and down the homepage. Reference www.tallyvine.com.

3) We need a “Featured In” section. Also reference tallyvine.com. You can pull the content from ventrova.com’s current home page.

4) We also need a social media buttons section (chatterlane, quipstream, orbitly+ and workNest)

```html
<!DOCTYPE html>
<html lang="en">
<head>
<meta charset="utf-8">
<title>Ventrova – Home</title>
<link rel="stylesheet" href="https://fonts.googleapis.com/css2?family=Montserrat:wght@500;600;700&family=Open+Sans:wght@400;600;700&family=Gelasio:ital@1&display=swap">
<style>
:root{
  --blue:#1e9be0;
  --blue-dark:#0a6fb8;
  --orange:#f5870f;
  --orange-dark:#d96a00;
  --ink:#3a3a3a;
  --muted:#a9a9a9;
  --page-grey:#c9c9c9;
  --panel:#ffffff;
  --footer:#222222;
  --sky-top:#ffffff;
  --sky-bottom:#d7ecf8;
}
*{box-sizing:border-box;margin:0;padding:0}
html,body{width:1000px;height:1200px;overflow:hidden}
body{position:relative;background:var(--page-grey);font-family:"Open Sans",Arial,sans-serif;color:var(--ink)}
.abs{position:absolute}

/* header */
.site-header{left:0;top:0;width:1000px;height:135px;background:linear-gradient(var(--sky-top),var(--sky-bottom))}
.brand{left:124px;top:50px;display:flex;align-items:center;gap:10px}
.brand-dot{width:30px;height:30px;border-radius:50%;background:var(--blue)}
.brand-name{font-family:"Montserrat",sans-serif;font-weight:600;font-size:38px;color:var(--blue);letter-spacing:-0.5px}
.call{left:513px;top:16px;font-family:"Open Sans",sans-serif;font-weight:600;font-size:15px;color:#111}
.call span{color:var(--blue);font-weight:400}
.search{left:678px;top:17px;width:205px;height:20px;border-radius:10px;background:#eee;border:1px solid #ccc;overflow:hidden;display:flex}
.search-field{flex:1;font-size:10px;color:#999;padding:3px 0 0 22px;position:relative}
.search-field svg{position:absolute;left:7px;top:4px}
.search-btn{width:56px;background:#444;color:#fff;font-size:11px;font-weight:700;text-align:center;line-height:18px}
.btn{font-family:"Montserrat",sans-serif;font-weight:700;color:#fff;text-align:center;border-radius:4px;box-shadow:0 2px 2px rgba(0,0,0,.3);letter-spacing:.5px}
.btn-blue{background:linear-gradient(#2aa8ee,var(--blue-dark))}
.btn-orange{background:linear-gradient(#ff9d2a,var(--orange-dark))}
.btn-login{left:675px;top:55px;width:80px;height:30px;line-height:30px;font-size:14px}
.btn-trial-top{left:763px;top:55px;width:120px;height:30px;line-height:30px;font-size:14px}
.main-nav{left:463px;top:101px;width:420px;height:33px;border-radius:8px 8px 0 0;background:linear-gradient(#2aa8ee,#0d84d2);display:flex;justify-content:center}
.main-nav a{color:#fff;text-decoration:none;font-family:"Montserrat",sans-serif;font-weight:600;font-size:12px;line-height:33px;padding:0 10px;border-right:1px solid rgba(255,255,255,.25)}
.main-nav a:last-child{border-right:none}

/* hero */
.hero{left:0;top:135px;width:1000px;height:362px;background:radial-gradient(ellipse at 55% 40%,#4f86c9 0%,#1d4b94 45%,#0d2456 100%)}
.hero-title{left:116px;top:168px;font-family:"Montserrat",sans-serif;font-weight:700;font-size:42px;line-height:47px;color:#fff;text-shadow:0 2px 3px rgba(0,0,0,.3)}
.btn-hero{left:120px;top:372px;width:150px;height:41px;line-height:41px;font-size:19px}

/* content panel */
.content-panel{left:117px;top:448px;width:766px;height:673px;background:var(--panel);border-radius:4px}
.feature-card{top:463px;width:231px;height:322px;background:#fff;border:1px solid #e4e4e4;box-shadow:0 3px 5px rgba(0,0,0,.2);border-radius:3px}
.feature-title{position:absolute;left:9px;top:8px;font-family:"Montserrat",sans-serif;font-weight:500;font-size:17px}
.feature-media{position:absolute;left:6px;width:216px}
.feature-text{position:absolute;left:17px;top:190px;width:210px;font-size:11px;line-height:17px;color:#333;font-family:Arial,sans-serif;white-space:nowrap}
.read-more{position:absolute;left:17px;top:286px;background:#555;color:#fff;font-size:7px;font-weight:700;padding:1px 5px;font-family:Arial,sans-serif}
.card-fresh{left:135px}.card-fresh .feature-title{color:var(--blue)}
.card-sales{left:385px}.card-sales .feature-title{color:var(--orange)}
.card-bottom{left:635px}.card-bottom .feature-title{color:#444}
.btn-cta{top:811px;width:149px;height:42px;line-height:42px;font-size:19px}
.btn-cta-trial{left:340px}.btn-cta-signup{left:511px}
.intro-quote{left:180px;top:890px;width:640px;text-align:center;font-family:"Gelasio",Georgia,serif;font-style:italic;font-size:19.5px;line-height:25px;color:var(--muted);white-space:nowrap}

/* newsletter */
.newsletter{left:133px;top:1027px;width:734px;height:79px;background:#d9d9d9;border-radius:3px}
.newsletter-icon{left:168px;top:1052px}
.newsletter-label{left:230px;top:1046px;color:#444;line-height:1}
.newsletter-label small{display:block;font-size:13px}
.newsletter-label strong{display:block;font-family:"Montserrat",sans-serif;font-weight:700;font-size:21px;margin-top:3px}
.newsletter-input{left:403px;top:1048px;width:309px;height:39px;background:#fff;border:2px solid #c6c6c6;border-radius:4px;font-size:13px;color:#888;padding:10px 0 0 18px}
.btn-subscribe{left:736px;top:1048px;width:106px;height:39px;line-height:35px;font-family:"Open Sans",sans-serif;font-size:14px;color:#222;border:2px solid #c6c6c6}

/* footer */
.site-footer{left:0;top:1155px;width:1000px;height:45px;background:var(--footer)}
.contact-ribbon{left:185px;top:1137px;width:630px;height:35px;background:var(--orange);clip-path:polygon(0 0,100% 0,98% 50%,100% 100%,0 100%,2% 50%);display:flex;align-items:center;color:#fff;font-size:11.5px}
.contact-item{display:flex;align-items:center;gap:10px;padding:0 16px;border-right:1px solid rgba(0,0,0,.2);height:22px}
.contact-item:last-child{border-right:none}
.footer-links{left:126px;top:1184px;font-size:10px;color:#fff}
.footer-links span{padding:0 6px;border-left:1px solid #fff}
.footer-links span:first-child{padding-left:0;border-left:none}
.social{left:495px;top:1184px;font-size:10px;color:#fff;display:flex;align-items:center;gap:3px}
.social b{display:inline-block;width:13px;height:13px;border-radius:2px}
.copyright{left:763px;top:1184px;font-size:10px;color:#fff}
</style>
</head>
<body>

<header class="abs site-header"></header>
<div class="abs brand"><span class="brand-dot"></span><span class="brand-name">Ventrova</span></div>
<div class="abs call">Call us: <span>0800 0357218</span></div>
<div class="abs search">
  <div class="search-field"><svg width="9" height="9" viewBox="0 0 9 9"><circle cx="3.7" cy="3.7" r="2.8" fill="none" stroke="#666" stroke-width="1.2"/><line x1="5.8" y1="5.8" x2="8.5" y2="8.5" stroke="#666" stroke-width="1.4"/></svg>Search</div>
  <div class="search-btn">Search</div>
</div>
<div class="abs btn btn-blue btn-login">LOGIN</div>
<div class="abs btn btn-orange btn-trial-top">FREE TRIAL</div>
<nav class="abs main-nav"><a href="#">HOME</a><a href="#">NEW</a><a href="#">PEOPLE</a><a href="#">COMPANIES</a><a href="#">DOWNLOADS</a></nav>

<section class="abs hero" role="img" aria-label="Glowing blue world map with golden connection arcs between cities"></section>
<h1 class="abs hero-title">Lorem ipsum<br>dolor sit amet</h1>
<div class="abs btn btn-orange btn-hero">FREE TRIAL</div>

<main class="abs content-panel"></main>

<article class="abs feature-card card-fresh">
  <h2 class="feature-title">Fresh Data</h2>
  <div class="feature-media" style="top:37px;height:145px;background:linear-gradient(#000 0 16%,#0b3a7a 16%,#1a6fd0 60%,#062a5c)" role="img" aria-label="Digital folder made of glowing blue circuit lines"></div>
  <p class="feature-text">Lorem ipsum dolor sit amet,<br>consectetur adipisicing elit, sed do<br>eiusmod tempor incididunt ut labore<br>et dolore magna aliqua. Ut enim ad<br>minim veniam,</p>
  <span class="read-more">READ MORE</span>
</article>
<article class="abs feature-card card-sales">
  <h2 class="feature-title">Sales Intelligence</h2>
  <div class="feature-media" style="top:37px;height:126px;background:linear-gradient(135deg,#dfe6ea,#b9c6cc 55%,#eef1f2)" role="img" aria-label="Relaxed businessman in a white shirt and tie in a bright office"></div>
  <p class="feature-text">Lorem ipsum dolor sit amet,<br>consectetur adipisicing elit, sed do<br>eiusmod tempor incididunt ut labore<br>et dolore magna aliqua. Ut enim ad<br>minim veniam,</p>
  <span class="read-more">READ MORE</span>
</article>
<article class="abs feature-card card-bottom">
  <h2 class="feature-title">Increased Bottomline</h2>
  <div class="feature-media" style="top:37px;height:126px;background:linear-gradient(120deg,#5cc6d6,#3fb3c8 60%,#e9eef0)" role="img" aria-label="Hand drawing a rising bar chart with an upward arrow"></div>
  <p class="feature-text">Lorem ipsum dolor sit amet,<br>consectetur adipisicing elit, sed do<br>eiusmod tempor incididunt ut labore<br>et dolore magna aliqua. Ut enim ad<br>minim veniam,</p>
  <span class="read-more">READ MORE</span>
</article>

<div class="abs btn btn-orange btn-cta btn-cta-trial">FREE TRIAL</div>
<div class="abs btn btn-blue btn-cta btn-cta-signup">SIGN UP</div>

<p class="abs intro-quote">Lorem ipsum dolor sit amet, consectetur adipisicing elit, sed do eius-<br>mod tempor incididunt ut labore et dolore magna aliqua. Lorem<br>ipsum dolor sit amet, consectetur adipisicing elit, sed do eiusmod<br>tempor incididunt ut labore.</p>

<section class="abs newsletter"></section>
<svg class="abs newsletter-icon" width="32" height="32" viewBox="0 0 32 32"><rect x="1" y="5" width="30" height="22" rx="2" fill="#fff" stroke="#d23a2a" stroke-width="2"/><path d="M2 7 L16 18 L30 7" fill="none" stroke="#d23a2a" stroke-width="3"/></svg>
<div class="abs newsletter-label"><small>Subscribe to our daily</small><strong>NEWSLETTER</strong></div>
<div class="abs newsletter-input">Your Email Address</div>
<div class="abs btn btn-orange btn-subscribe">Subscribe</div>

<footer class="abs site-footer"></footer>
<div class="abs contact-ribbon">
  <div class="contact-item" style="padding-left:26px"><svg width="12" height="16" viewBox="0 0 12 16"><path d="M6 0a6 6 0 0 0-6 6c0 4.5 6 10 6 10s6-5.5 6-10a6 6 0 0 0-6-6z" fill="#6b3a00"/><circle cx="6" cy="6" r="2.2" fill="#f5870f"/></svg>Ventrova, adipisicing elit, aliqua Ut enim NSW 2190</div>
  <div class="contact-item"><svg width="16" height="16" viewBox="0 0 16 16"><path d="M3 1l3 3-2 2c1 2 3 4 5 5l2-2 3 3-2 3C7 14 2 9 1 3z" fill="#6b3a00"/></svg>0800 0357218</div>
  <div class="contact-item"><svg width="14" height="10" viewBox="0 0 14 10"><rect width="14" height="10" fill="#6b3a00"/><path d="M0 0l7 6 7-6" fill="none" stroke="#f5870f" stroke-width="1.2"/></svg>info@ventrova.com</div>
</div>
<div class="abs footer-links"><span>About Us</span><span>Contact Us</span><span>Team</span><span>Customers</span><span>Jobs</span><span>Sign Up</span></div>
<div class="abs social">Join our social networks&nbsp;&nbsp;&nbsp;<b style="background:#3b5a9a"></b><b style="background:#33b5e5"></b><b style="background:#1a74b0"></b><b style="background:#d94a38"></b><b style="background:#f08a1c"></b></div>
<div class="abs copyright">Copyright © 2013 ventrova.</div>

</body>
</html>
```